Business Card Design Project

We need a business card design for our company kB7 s.r.o. The company is based in Slovakia and selling massage, yoga and meditation accessories online and offline. At the place where the offices are, we have a yoga studio, massage room, show room and shop as well. We will give the business card for customers who visit our shop or show room personally and for the new suppliers of demanded products we are visiting in the future.
I would like to have:
- small logo and datas on one side
- big logo and our main e-shops on the other side:
- www.pohodlnelavice.sk
- www.relaxnipultiky.cz
Datas:
Peter Kolar, MSc. / CEO
kB7 s.r.o.
Borovicová 742/3
938 05 Dunajská Streda
Slovak republic (Slovakia)
Office tel.: +421 (0) 917 604 382
Private tel.: +421 (0) 911 758 026
E-mail: info@kb7.sk
Web: www.kb7.sk
It is up to you if you use graphics emphasizing our profile or leave it simple and modern without pics. Looking forward to receiving your designs! Thank You!

```html
<!DOCTYPE html>
<html lang="en">
<head>
<meta charset="utf-8">
<title>kB7 s.r.o. – Business Card</title>
<link rel="stylesheet" href="https://fonts.googleapis.com/css2?family=Lato:wght@400;700&display=swap">
<style>
  :root {
    --orange: #f2801f;
    --black: #161616;
    --card-dark: #1c1c1c;
    --grey-logo: #7f8993;
    --grey-url: #8d8d8d;
    --white: #ffffff;
    --ink: #1a1a1a;
    --rule: #4a4a4a;
    --stage: #3b3b3d;
  }
  * { margin: 0; padding: 0; box-sizing: border-box; }
  html, body {
    width: 1200px; height: 926px; overflow: hidden;
    background: var(--stage);
    font-family: "Lato", sans-serif;
  }
  .card {
    position: absolute; left: 290px;
    width: 620px; height: 300px;
    border-radius: 16px; overflow: hidden;
  }
  .card-back { top: 110px; background: var(--card-dark); }
  .card-front { top: 500px; background: var(--white); }
  .card-shape { position: absolute; inset: 0; }

  /* back side */
  .brand-large {
    position: absolute; left: 0; right: 0; top: 90px;
    text-align: center;
  }
  .brand-large .brand-name {
    font-weight: 700; font-size: 92px; line-height: 1; color: var(--grey-logo);
  }
  .eshops {
    position: absolute; left: 0; right: 0; top: 218px;
    text-align: center; color: var(--grey-url);
    font-size: 15px; letter-spacing: 1.2px;
  }
  .accent-bar {
    position: absolute; left: 32px; right: 32px; top: 256px;
    height: 6px; border-radius: 3px; background: var(--orange);
  }

  /* front side */
  .side-bar {
    position: absolute; left: 40px; top: 38px;
    width: 7px; height: 228px; border-radius: 4px; background: var(--orange);
  }
  .contact-list { position: absolute; left: 58px; top: 54px; width: 262px; color: var(--ink); font-size: 15px; }
  .contact-row {
    display: flex; align-items: center; gap: 10px;
    padding: 6px 0 8px; border-bottom: 1.5px solid var(--rule);
  }
  .contact-row:last-child { border-bottom: none; padding-top: 12px; }
  .contact-icon { width: 16px; height: 16px; flex: none; fill: var(--ink); }
  .contact-lines { line-height: 1.2; }
  .contact-lines .label { display: inline-block; width: 62px; }
  .address { line-height: 1.3; }

  .holder {
    position: absolute; left: 378px; top: 52px; color: var(--white);
  }
  .holder-name { font-size: 19px; font-weight: 400; }
  .holder-name strong { font-weight: 700; }
  .holder-name .title { font-size: 13px; }
  .holder-company { font-size: 13px; font-weight: 700; margin-top: 2px; }
  .brand-small {
    position: absolute; left: 455px; top: 186px;
  }
  .brand-small .brand-name { font-weight: 700; font-size: 62px; line-height: 1; color: var(--white); }
</style>
</head>
<body>

<section class="card card-back">
  <svg class="card-shape" width="620" height="300" viewBox="0 0 620 300">
    <rect width="620" height="70" fill="var(--orange)"/>
    <path d="M0,58 Q150,22 290,40 L300,28 L310,40 L320,28 L330,40 Q470,22 620,62 L620,300 L0,300 Z" fill="var(--card-dark)"/>
  </svg>
  <div class="brand-large">
    <span class="brand-name">kB7</span>
  </div>
  <p class="eshops">www.pohodlnelavice.sk / www.relaxnipultiky.cz</p>
  <div class="accent-bar"></div>
</section>

<section class="card card-front">
  <svg class="card-shape" width="620" height="300" viewBox="0 0 620 300">
    <path d="M326,0 C352,60 356,118 342,146 L312,162 L344,170 C322,222 322,262 336,300 L620,300 L620,0 Z" fill="var(--black)"/>
    <path d="M334,0 C360,60 364,118 350,146 L320,162 L352,170 C330,222 330,262 344,300 L620,300 L620,0 Z" fill="var(--orange)"/>
  </svg>

  <div class="side-bar"></div>

  <div class="contact-list">
    <div class="contact-row">
      <svg class="contact-icon" viewBox="0 0 16 16"><path d="M2,6 Q8,1 14,6 L12,8 L10,6.5 L6,6.5 L4,8 Z M4,9 H12 L13,14 H3 Z"/></svg>
      <div class="contact-lines">
        <div><span class="label">Office</span>+421 (0) 917 604 382</div>
        <div><span class="label">Private</span>+421 (0) 911 758 026</div>
      </div>
    </div>
    <div class="contact-row">
      <svg class="contact-icon" viewBox="0 0 16 16"><path d="M1,3 H15 V13 H1 Z M2,4 L8,9 L14,4 Z" fill-rule="evenodd"/></svg>
      <div class="contact-lines"><span class="label">E-mail</span>info@kb7.sk</div>
    </div>
    <div class="contact-row">
      <svg class="contact-icon" viewBox="0 0 16 16"><path d="M1,2 H15 V11 H1 Z M2.5,3.5 V9.5 H13.5 V3.5 Z M6,12 H10 V13 H12 V14.5 H4 V13 H6 Z" fill-rule="evenodd"/></svg>
      <div class="contact-lines"><span class="label">Web</span>www.kb7.sk</div>
    </div>
    <div class="contact-row">
      <svg class="contact-icon" viewBox="0 0 16 16"><path d="M8,1 C4.7,1 3,3.5 3,6 C3,9.5 8,15 8,15 C8,15 13,9.5 13,6 C13,3.5 11.3,1 8,1 Z M8,4.2 A1.8,1.8 0 1 0 8,7.8 A1.8,1.8 0 1 0 8,4.2 Z" fill-rule="evenodd"/></svg>
      <div class="contact-lines address">
        Borovicová 742/3,<br>
        938 05 Dunajská Streda,<br>
        Slovak republic (Slovakia)
      </div>
    </div>
  </div>

  <div class="holder">
    <p class="holder-name">Peter <strong>Kolar</strong>, <span class="title">MSc. / CEO</span></p>
    <p class="holder-company">kB7 s.r.o.</p>
  </div>

  <div class="brand-small">
    <span class="brand-name">kB7</span>
  </div>
</section>

</body>
</html>
```